Web Design Project for Communications Agency

The design I need (PSD file) is for an agency offering specialised PR and communications services for customers in the healthcare sector.

OBJECTIVES OF THE WEBSITE:
1. To promote the agency's communication services
2. To position Pellerin Dautry as an industry leader, an expert in healthcare PR and communications by highlighting blogposts and social media.

WHAT I NEED:
1st, I need the design for the Home Page ONLY.
Once approved, I will need the other pages designed as well. (Here is prototype that we've already developed for the Website that will guide you in the design:
http://velocraft.example/pellerindautry/)

VISUAL INSPIRATION
We want to give this Website a "Flat Design" look. Here are some websites for inspiration :
- http://marbleforge.example/#!/process
- http://www.brisklane.example/
- http://tovalinework.example/

Also, reuse images found on the company's current Website :
http://www.pellerindautry.example/fr/index.html

HOMEPAGE MAIN ELEMENTS:
1. Main menu : 6 sections
Accueil | Agence | Services | Approche | Publications | Contact

2. Main Call To Action (big dark rectangle in prototype):
Can be slider or just an information bloc.

3. Publications récentes :
The 4 latest blog posts must be features on the homepage (will be linked with the "Publications" section)

4. Dynamic Footer :
Contains a Chirpline feed and a Subscribe to our Newsletter feature (revecez nos publications)

OTHER PAGES (to design once Homepage is approved)
- Agence (about us)
- Services (our team)
- Approche (our approach)
- Publications (blog articles)
- Contact (Contact us)

• Please refer to prototype :
http://velocraft.example/pellerindautry/
Must have ALL features present in prototype.

Also, must reuse this picture in the design : http://pellerindautry.example/static/images/home-big-box.jpg

Finally, you will find attached the company logo.

```html
<!DOCTYPE html>
<html lang="fr">
<head>
<meta charset="utf-8">
<title>Pellerin Dautry — Accueil</title>
<link href="https://fonts.googleapis.com/css2?family=Maven+Pro:wght@400;500;700&family=Roboto+Slab:wght@400;700&display=swap" rel="stylesheet">
<style>
:root{
  --red:#d8323a;
  --red-dark:#b8242b;
  --hero:#414042;
  --ink:#333;
  --muted:#555;
  --nav-bg:#e4e4e4;
  --footer-bg:#e1e0e1;
  --white:#fff;
}
*{margin:0;padding:0;box-sizing:border-box}
html,body{width:1200px;height:1000px;overflow:hidden;background:var(--white)}
body{position:relative;font-family:"Maven Pro",sans-serif;color:var(--ink)}
.page{position:absolute;left:152px;top:0;width:896px;height:1000px}
.abs{position:absolute}

.header{left:0;top:0;width:896px;height:52px;background:linear-gradient(#fff,#ececec)}
.brand{left:229px;top:20px;color:var(--red);font-family:"Maven Pro",sans-serif;font-weight:500;font-size:16px;line-height:18px;white-space:nowrap}
.social{top:11px;width:15px;height:15px;border-radius:2px}
.lang{left:591px;top:11px;width:77px;height:15px;border:1px solid #ccc;background:#fff;font-size:6px;color:#999;padding:3px 4px}
.lang::after{content:"";position:absolute;right:0;top:0;width:12px;height:13px;background:#e8e8e8;border-left:1px solid #ccc}

.nav{left:0;top:52px;width:896px;height:17px;background:var(--nav-bg);border-top:1px solid #d4d4d4}
.nav-item{top:0;height:17px;line-height:15px;font-size:8px;font-weight:500;color:#444;text-align:center;transform:translateX(-50%);white-space:nowrap}
.nav-active{left:339px;top:45px;width:53px;height:24px;background:var(--hero);border-radius:3px 3px 0 0;color:#fff;font-size:8px;font-weight:500;text-align:center;line-height:28px}

.hero{left:0;top:69px;width:896px;height:186px;background:var(--hero)}
.hero-title{left:229px;top:12px;width:248px;color:#fff;font-size:20px;line-height:25px;font-weight:400}
.btn{background:linear-gradient(#e0434a,var(--red-dark));color:#fff;font-weight:700;border-radius:3px;box-shadow:0 2px 4px rgba(0,0,0,.3);white-space:nowrap}
.hero-btn{left:369px;top:137px;width:110px;height:26px;font-size:11px;line-height:26px;padding-left:8px}
.btn svg{position:absolute;right:7px;top:50%;transform:translateY(-50%)}
.hero-visual{left:496px;top:10px;width:168px;height:170px;background:radial-gradient(circle at 45% 35%,#f5f5f5 0,#d8d8d8 45%,rgba(200,0,20,0) 70%),linear-gradient(135deg,#c8202c 0,#e6e6e6 55%,#414042 100%);border-radius:10px;opacity:.9}

.section-title{left:228px;top:262px;font-family:"Roboto Slab",serif;font-weight:700;font-size:19px;color:var(--red)}
.post{left:229px;width:440px;height:100px}
.post-photo{left:0;top:0;width:139px;height:90px;border:2px solid #fff;box-shadow:0 1px 3px rgba(0,0,0,.35)}
.post-title{left:149px;top:-2px;font-family:"Roboto Slab",serif;font-weight:700;font-size:7.5px;color:#222}
.post-date{left:149px;top:10px;font-family:"Roboto Slab",serif;font-style:italic;font-size:5px;color:var(--red)}
.post-body{left:149px;top:27px;width:291px;font-family:"Roboto Slab",serif;font-size:5.6px;line-height:9.8px;color:#444}
.post-more{right:0;top:83px;font-family:"Roboto Slab",serif;font-size:5.5px;color:var(--red);white-space:nowrap}

.footer{left:0;top:778px;width:896px;height:222px;background:var(--footer-bg);border-top:3px solid var(--red)}
.feed-name{left:229px;top:26px;font-family:"Maven Pro",sans-serif;font-weight:500;font-size:22px;color:var(--ink)}
.tweet{left:229px;width:180px;font-size:7px;line-height:10px;color:#555}
.tweet span{color:var(--red)}
.signup-title{left:452px;top:33px;font-family:"Roboto Slab",serif;font-weight:700;font-size:13px;color:var(--red);white-space:nowrap}
.label{left:452px;font-size:10.5px;color:#444}
.field{left:452px;width:179px;height:23px;background:#fff;border:1px solid #777}
.signup-btn{left:521px;top:160px;width:110px;height:28px;font-size:11px;line-height:28px;padding-left:7px}
</style>
</head>
<body>
<div class="page">
  <header class="abs header"></header>
  <div class="abs brand">Pellerin Dautry</div>
  <div class="abs social" style="left:534px;background:#48b8e6" role="img" aria-label="Chirpline"></div>
  <div class="abs social" style="left:553px;background:#2a7bb8" role="img" aria-label="Linkfold"></div>
  <div class="abs social" style="left:572px;background:#e0703a" role="img" aria-label="Tumblebee"></div>
  <div class="abs lang">Select Language</div>

  <nav class="abs nav">
    <span class="abs nav-item" style="left:418px">Agence</span>
    <span class="abs nav-item" style="left:471px">Services</span>
    <span class="abs nav-item" style="left:529px">Approche</span>
    <span class="abs nav-item" style="left:594px">Publications</span>
    <span class="abs nav-item" style="left:655px">Contact</span>
  </nav>
  <div class="abs nav-active">Accueil</div>

  <section class="abs hero">
    <h1 class="abs hero-title">Cabinet-conseil en communications et affaires publiques spécialisé dans le secteur de la santé.</h1>
    <div class="abs btn hero-btn">En Savoir Plus
      <svg width="8" height="10" viewBox="0 0 8 10"><path d="M1 1l4 4-4 4" fill="none" stroke="#fff" stroke-width="2"/></svg>
    </div>
    <div class="abs hero-visual" role="img" aria-label="Cube blanc orné d'une croix rouge"></div>
  </section>

  <h2 class="abs section-title">Publication récentes</h2>

  <article class="abs post" style="top:300px">
    <div class="abs post-photo" role="img" aria-label="Portrait de la fondatrice" style="background:linear-gradient(135deg,#d9c7b4,#8a6a58 60%,#3b2a24)"></div>
    <h3 class="abs post-title">Titre de la publication</h3>
    <div class="abs post-date">23 juillet 2013</div>
    <p class="abs post-body">Lorem ipsum dolor sit amet, consectetur adipisicing elit, sed do eiusmod tempor incididunt ut labore et dolore magna aliqua. Ut enim ad minim veniam, quis nostrud exercitation ullamco laboris nisi ut aliquip ex ea commodo consequat. Duis aute irure dolor in reprehenderit in voluptate velit esse cillum dolore eu fugiat nulla pariatur. Velit esse cillum dolore eu fugiat nulla pariatur. Excepteur sint occaecat cupidatat non proident, sunt in culpa qui officia deserunt mollit anim id est laborum.</p>
    <a class="abs post-more">Article complet »</a>
  </article>

  <article class="abs post" style="top:417px">
    <div class="abs post-photo" role="img" aria-label="Microphones de conférence de presse" style="background:linear-gradient(#f2f2f2,#e6e6e6 50%,#555)"></div>
    <h3 class="abs post-title">Titre de la publication</h3>
    <div class="abs post-date">23 juillet 2013</div>
    <p class="abs post-body">Lorem ipsum dolor sit amet, consectetur adipisicing elit, sed do eiusmod tempor incididunt ut labore et dolore magna aliqua. Ut enim ad minim veniam, quis nostrud exercitation ullamco laboris nisi ut aliquip ex ea commodo consequat. Duis aute irure dolor in reprehenderit in voluptate velit esse cillum dolore eu fugiat nulla pariatur. Velit esse cillum dolore eu fugiat nulla pariatur. Excepteur sint occaecat cupidatat non proident, sunt in culpa qui officia deserunt mollit anim id est laborum.</p>
    <a class="abs post-more">Article complet »</a>
  </article>

  <article class="abs post" style="top:534px">
    <div class="abs post-photo" role="img" aria-label="Mains levées dans une assemblée" style="background:linear-gradient(#f0e4d8,#c9926a 50%,#2e2622)"></div>
    <h3 class="abs post-title">Titre de la publication</h3>
    <div class="abs post-date">23 juillet 2013</div>
    <p class="abs post-body">Lorem ipsum dolor sit amet, consectetur adipisicing elit, sed do eiusmod tempor incididunt ut labore et dolore magna aliqua. Ut enim ad minim veniam, quis nostrud exercitation ullamco laboris nisi ut aliquip ex ea commodo consequat. Duis aute irure dolor in reprehenderit in voluptate velit esse cillum dolore eu fugiat nulla pariatur. Velit esse cillum dolore eu fugiat nulla pariatur. Excepteur sint occaecat cupidatat non proident, sunt in culpa qui officia deserunt mollit anim id est laborum.</p>
    <a class="abs post-more">Article complet »</a>
  </article>

  <article class="abs post" style="top:651px">
    <div class="abs post-photo" role="img" aria-label="Portrait de la fondatrice" style="background:linear-gradient(135deg,#d9c7b4,#8a6a58 60%,#3b2a24)"></div>
    <h3 class="abs post-title">Titre de la publication</h3>
    <div class="abs post-date">23 juillet 2013</div>
    <p class="abs post-body">Lorem ipsum dolor sit amet, consectetur adipisicing elit, sed do eiusmod tempor incididunt ut labore et dolore magna aliqua. Ut enim ad minim veniam, quis nostrud exercitation ullamco laboris nisi ut aliquip ex ea commodo consequat. Duis aute irure dolor in reprehenderit in voluptate velit esse cillum dolore eu fugiat nulla pariatur. Velit esse cillum dolore eu fugiat nulla pariatur. Excepteur sint occaecat cupidatat non proident, sunt in culpa qui officia deserunt mollit anim id est laborum.</p>
    <a class="abs post-more">Article complet »</a>
  </article>

  <footer class="abs footer">
    <div class="abs feed-name">Chirpline</div>
    <p class="abs tweet" style="top:66px">Velit esse cillum dolore eu fugiat nulla pariatur. Excepteur sint occaecat cupidatat non proident. <span>@PellerinDautry #EnjeuSanté</span></p>
    <p class="abs tweet" style="top:118px">Velit esse eu fugiat nulla pariatur. Excepteur sint occaecat cupidatat non proident. <span>@PellerinDautry #EnjeuSanté</span></p>
    <p class="abs tweet" style="top:156px">Velit esse cillum dolore eu fugiat nulla pariatur. Excepteur sint occaecat cupidatat non proident. <span>@PellerinDautry #EnjeuSanté</span></p>

    <h2 class="abs signup-title">Recevez nos publications</h2>
    <label class="abs label" style="top:66px">Votre nom</label>
    <div class="abs field" style="top:81px"></div>
    <label class="abs label" style="top:113px">Votre courriel</label>
    <div class="abs field" style="top:128px"></div>
    <div class="abs btn signup-btn">Abonnez-vous
      <svg width="8" height="10" viewBox="0 0 8 10"><path d="M1 1l4 4-4 4" fill="none" stroke="#fff" stroke-width="2"/></svg>
    </div>
  </footer>
</div>
</body>
</html>
```